Tandor8Vale

I need a website designed to feature a new product for my company. I am dedicating a separate site just highlight the program. The url will be tandor8vale.com and the product name is tandor vale. The product is ringless voicemail. We take a recorded script and send it to our clients customers cell phones without the phone ringing.

The site will consist of a home page. I animated video demo. It will house 18 scripts and voice overs to match, a results page, and a page to request a live demo.

We sell the product to new car dealerships

```html
<!DOCTYPE html>
<html lang="en">
<head>
<meta charset="utf-8">
<title>Tandor8Vale – Ringless Voicemail</title>
<link rel="stylesheet" href="https://fonts.googleapis.com/css2?family=Jost:wght@400;500;600&family=Open+Sans:ital,wght@0,400;0,600;0,700;1,400&display=swap">
<style>
:root{
  --navy:#1d4270;
  --navy-dark:#173a63;
  --orange:#f26f21;
  --ink:#2b2b2b;
  --text:#666a70;
  --muted:#8a8e94;
  --band:#eef1f5;
  --line:#d9dde2;
  --green:#5cb85c;
  --white:#ffffff;
}
*{margin:0;padding:0;box-sizing:border-box}
html,body{width:1200px;height:2436px;overflow:hidden}
body{position:relative;background:var(--white);font-family:"Open Sans",Arial,sans-serif;color:var(--text)}
.abs{position:absolute}
.heading{font-family:"Jost","Futura",sans-serif;color:var(--ink);font-weight:500}

/* top bar */
.topbar{left:0;top:0;width:1200px;height:26px;background:var(--navy)}
.topbar-info{right:120px;top:0;height:26px;display:flex;align-items:center;gap:10px;color:#fff;font-size:12px}
.topbar-info svg{vertical-align:-2px;margin-right:5px}
.login{background:var(--navy-dark);height:26px;padding:0 14px;display:flex;align-items:center;font-weight:600;margin-left:12px}

/* header */
.brand{left:99px;top:50px;font-family:"Jost",sans-serif;font-weight:500;font-size:35px;color:var(--navy);letter-spacing:-.3px}
.nav{top:58px;font-size:17px;color:#222;font-weight:500;font-family:"Open Sans",sans-serif}
.nav.active{color:var(--orange)}

/* hero */
.hero{left:0;top:107px;width:1200px;height:487px;background:linear-gradient(100deg,#4a3a5a 0%,#6a5a6e 35%,#8f8a8c 60%,#5a6170 100%)}
.hero-title{left:99px;top:238px;font-family:"Jost",sans-serif;font-size:54px;color:#fff;font-weight:400}
.hero-rule{left:99px;top:313px;width:526px;height:2px;background:#fff}
.hero-text{left:99px;top:332px;width:540px;font-size:18.5px;line-height:28px;color:#fff}
.btn-hero{left:99px;top:411px;width:193px;height:39px;background:var(--orange);color:#fff;font-size:14.5px;font-weight:700;display:flex;align-items:center;justify-content:center}
.dots{left:566px;top:527px;display:flex;gap:6px}
.dots span{width:15px;height:15px;border-radius:50%;background:#fff}
.dots span.on{background:var(--navy)}

/* welcome */
.welcome-title{left:0;width:1200px;top:638px;text-align:center;font-size:29px}
.welcome-text{left:250px;width:700px;top:690px;text-align:center;font-size:12.5px;line-height:24px}
.feature{top:765px;width:160px;height:160px}
.feature-label{top:936px;width:260px;text-align:center;font-size:21px;color:#222}

/* how it works */
.how{left:0;top:1021px;width:1200px;height:444px;background:var(--band)}
.how-title{left:99px;top:1050px;font-size:28px}
.steps{left:99px;top:1108px;width:520px;list-style:none}
.steps li{display:flex;font-size:12.5px;line-height:16px;color:var(--text)}
.steps .num{font-family:"Jost",sans-serif;font-weight:600;font-size:18px;color:#555;width:24px;flex:none;line-height:18px}
.read-more{font-size:12.5px;font-weight:700;color:var(--orange)}
.video{left:645px;top:1101px;width:459px;height:284px;background:var(--green);border-top:9px solid #2e3033;border-bottom:12px solid #2e3033}

/* offer */
.offer-art{left:99px;top:1502px;width:390px;height:374px;background:linear-gradient(180deg,#eef3f7,#dfe8ef);border-radius:6px}
.offer-title{left:594px;top:1530px;font-size:30px}
.offer-list{left:594px;top:1590px;width:520px;list-style:none}
.offer-list li{position:absolute;left:0;display:flex;font-size:13px;line-height:21px;width:520px}
.offer-list svg{flex:none;margin:3px 12px 0 0}
.btn-outline{left:594px;top:1811px;width:132px;height:38px;border:1.5px solid #c9ccd0;color:var(--orange);font-size:12.5px;font-weight:700;display:flex;align-items:center;justify-content:center}

/* testimonial */
.quote-band{left:0;top:1920px;width:1200px;height:207px;background:var(--orange)}
.avatar{left:131px;top:1960px;width:124px;height:124px;border-radius:50%;border:5px solid #fff;background:linear-gradient(160deg,#b9b2ab,#6f7782)}
.quote-rule{left:289px;top:1958px;width:1px;height:126px;background:rgba(255,255,255,.7)}
.quote-text{left:322px;top:1962px;width:780px;font-style:italic;color:#fff;font-size:14.5px;line-height:29px}
.quote-name{left:326px;top:2068px;color:#fff;font-weight:700;font-size:15px}

/* footer */
.foot-brand{left:99px;top:2228px;font-family:"Jost",sans-serif;font-weight:500;font-size:36px;color:var(--navy)}
.foot-col{top:2170px}
.foot-col h4{font-family:"Jost",sans-serif;font-weight:500;font-size:19px;color:#222;margin-bottom:10px}
.foot-col ul{list-style:none}
.foot-col li{font-size:12.5px;line-height:23px;color:var(--text)}
.contact li{display:flex;line-height:18px;margin-bottom:14px}
.contact svg{flex:none;margin:1px 14px 0 0}
.contact a{color:var(--text)}
.foot-rule{left:99px;top:2374px;width:1002px;height:1px;background:var(--line)}
.copyright{left:99px;top:2400px;font-size:12.5px}
.social{top:2394px;display:flex;gap:8px;left:958px}
.social span{width:30px;height:30px;border-radius:50%;border:1.5px solid var(--navy)}
</style>
</head>
<body>

<div class="abs topbar"></div>
<div class="abs topbar-info">
  <span><svg width="11" height="11" viewBox="0 0 24 24"><path fill="#fff" d="M6.6 10.8a15 15 0 006.6 6.6l2.2-2.2a1 1 0 011-.25 11.4 11.4 0 003.6.57 1 1 0 011 1V20a1 1 0 01-1 1A17 17 0 013 4a1 1 0 011-1h3.5a1 1 0 011 1c0 1.25.2 2.45.57 3.57a1 1 0 01-.25 1z"/></svg>555 014 2280</span>
  <span>|</span>
  <span><svg width="12" height="10" viewBox="0 0 24 18"><rect width="24" height="18" rx="2" fill="#fff"/><path d="M1 2l11 8 11-8" stroke="#1d4270" stroke-width="2" fill="none"/></svg>info@tandor8vale.com</span>
  <span class="login"><svg width="10" height="11" viewBox="0 0 20 22"><rect y="9" width="20" height="13" rx="2" fill="#fff"/><path d="M5 9V6a5 5 0 0110 0v3" stroke="#fff" stroke-width="3" fill="none"/></svg>Login</span>
</div>

<div class="abs brand">Tandor8Vale</div>
<div class="abs nav active" style="left:460px">Home</div>
<div class="abs nav" style="left:544px">About us</div>
<div class="abs nav" style="left:649px">Products</div>
<div class="abs nav" style="left:752px">How it works</div>
<div class="abs nav" style="left:888px">News</div>
<div class="abs nav" style="left:968px">Contact us</div>
<svg class="abs" style="left:1086px;top:61px" width="18" height="18" viewBox="0 0 24 24"><circle cx="10" cy="10" r="7" stroke="#222" stroke-width="3" fill="none"/><path d="M15 15l6 6" stroke="#222" stroke-width="3.5" stroke-linecap="round"/></svg>

<div class="abs hero" role="img" aria-label="Photo of a smiling young man sitting on outdoor steps talking on a mobile phone"></div>
<div class="abs hero-title">Tandor 8 Vale</div>
<div class="abs hero-rule"></div>
<p class="abs hero-text">We take a recorded script and send it to our clients customers cell phones without the phone ringing.</p>
<div class="abs btn-hero">FIND OUT MORE &gt;&gt;</div>
<div class="abs dots"><span class="on"></span><span></span><span></span><span></span></div>

<h2 class="abs heading welcome-title">Welcome to Tandor8Vale</h2>
<p class="abs welcome-text">At vero eos et accusamus et iusto odio dignissimos ducimus qui blanditiis praesentium voluptatum deleniti atque corrupti quos dolores et quas molestias excepturi sint occaecati cupiditate non provident, similique sunt</p>

<svg class="abs feature" style="left:118px" viewBox="0 0 160 160"><rect x="25" y="25" width="110" height="110" transform="rotate(45 80 80)" fill="none" stroke="#222" stroke-width="1.5"/><path d="M54 80l54-24-18 52-10-18z" fill="#1d4270"/><path d="M80 90l28-34" stroke="#fff" stroke-width="2"/></svg>
<div class="abs feature-label" style="left:68px">Fast</div>

<svg class="abs feature" style="left:386px" viewBox="0 0 160 160"><rect x="25" y="25" width="110" height="110" transform="rotate(45 80 80)" fill="none" stroke="#222" stroke-width="1.5"/><rect x="58" y="60" width="40" height="40" rx="5" fill="none" stroke="#1d4270" stroke-width="5"/><path d="M66 78l12 12 26-30" fill="none" stroke="#1d4270" stroke-width="7" stroke-linecap="round" stroke-linejoin="round"/></svg>
<div class="abs feature-label" style="left:336px">Effective</div>

<svg class="abs feature" style="left:654px" viewBox="0 0 160 160"><rect x="25" y="25" width="110" height="110" transform="rotate(45 80 80)" fill="none" stroke="#222" stroke-width="1.5"/><rect x="52" y="64" width="56" height="32" fill="#1d4270"/><rect x="58" y="70" width="44" height="20" fill="#fff"/><circle cx="80" cy="80" r="8" fill="#1d4270"/></svg>
<div class="abs feature-label" style="left:604px">Inexpensive</div>

<svg class="abs feature" style="left:924px" viewBox="0 0 160 160"><rect x="25" y="25" width="110" height="110" transform="rotate(45 80 80)" fill="none" stroke="#222" stroke-width="1.5"/><path d="M52 58v44h56" fill="none" stroke="#1d4270" stroke-width="3"/><rect x="59" y="80" width="7" height="18" fill="#1d4270"/><rect x="70" y="72" width="7" height="26" fill="#1d4270"/><rect x="81" y="77" width="7" height="21" fill="#1d4270"/><rect x="92" y="66" width="7" height="32" fill="#1d4270"/></svg>
<div class="abs feature-label" style="left:874px">Versatile Marketing</div>

<section class="abs how"></section>
<h2 class="abs heading how-title">How It Works</h2>
<ol class="abs steps">
  <li style="margin-bottom:14px"><span class="num">1.</span><span>We select a targeted list of past sales customers, service customers, or unsold leads.</span></li>
  <li style="margin-bottom:10px"><span class="num">2.</span><span>We develop and record a script based on your stores current needs, incentives, time of year, and list.</span></li>
  <li style="margin-bottom:10px"><span class="num">3.</span><span>Your team will be coached and given a set of scripted responses to be sure everyone is prepared.</span></li>
  <li style="margin-bottom:14px"><span class="num">4.</span><span>Your message and list are uploaded to our system and delivered at any speed you wish.</span></li>
  <li style="margin-bottom:14px"><span class="num">5.</span><span>Inbound return calls will begin within minutes.</span></li>
  <li style="margin-bottom:14px"><span class="num">6.</span><span>This program requires zero set up.</span></li>
  <li style="margin-bottom:14px"><span class="num">7.</span><span>The simple process above can be completed and go live in as little as 24 hours.</span></li>
  <li style="margin-bottom:22px"><span class="num">8.</span><span>Every inbound phone call is recorded, tracked, and caller id information is captured.</span></li>
  <li><span class="read-more">READ MORE &gt;&gt;</span></li>
</ol>
<div class="abs video" role="img" aria-label="Demo video still: world map with a cloud linking two mobile phones"></div>
<svg class="abs" style="left:843px;top:1213px" width="62" height="62" viewBox="0 0 62 62"><circle cx="31" cy="31" r="31" fill="#3b3d40"/><path d="M24 18l22 13-22 13z" fill="#fff"/></svg>

<div class="abs offer-art" role="img" aria-label="Illustration of two smartphones showing a man and a woman chatting, linked by a globe"></div>
<h2 class="abs heading offer-title">The Offer</h2>
<ul class="abs offer-list">
  <li style="top:0"><svg width="15" height="15" viewBox="0 0 16 16"><circle cx="8" cy="8" r="8" fill="#f26f21"/><path d="M4.5 8.2l2.3 2.3 4.7-4.8" stroke="#fff" stroke-width="2" fill="none"/></svg><span>We can use this as a buy back offer, re-engage unsold CRM leads, offer monthly factory incentives, inform of a sales event, or to get CSI surveys completed</span></li>
  <li style="top:68px"><svg width="15" height="15" viewBox="0 0 16 16"><circle cx="8" cy="8" r="8" fill="#f26f21"/><path d="M4.5 8.2l2.3 2.3 4.7-4.8" stroke="#fff" stroke-width="2" fill="none"/></svg><span>It can be recorded by anyone!</span></li>
  <li style="top:112px"><svg width="15" height="15" viewBox="0 0 16 16"><circle cx="8" cy="8" r="8" fill="#f26f21"/><path d="M4.5 8.2l2.3 2.3 4.7-4.8" stroke="#fff" stroke-width="2" fill="none"/></svg><span>Works because the message is perfect every time!</span></li>
  <li style="top:156px"><svg width="15" height="15" viewBox="0 0 16 16"><circle cx="8" cy="8" r="8" fill="#f26f21"/><path d="M4.5 8.2l2.3 2.3 4.7-4.8" stroke="#fff" stroke-width="2" fill="none"/></svg><span>The information stays with them!</span></li>
</ul>
<div class="abs btn-outline">READ MORE &gt;&gt;</div>

<section class="abs quote-band"></section>
<div class="abs avatar" role="img" aria-label="Portrait photo of the customer giving the testimonial"></div>
<div class="abs quote-rule"></div>
<p class="abs quote-text">At vero eos et accusamus et iusto odio dignissimos ducimus qui blanditiis praesentium voluptatum deleniti atque corrupti quos dolores et quas molestias excepturi sint occaecati cupiditate non provident, similique sunt in culpa qui officia deserunt mollitia animi, id est</p>
<div class="abs quote-name">MARCUS ELLERY</div>

<div class="abs foot-brand">Tandor8Vale</div>
<div class="abs foot-col" style="left:406px"><h4>About us</h4><ul><li>Our Story</li><li>Team</li><li>Newsletters</li><li>Contact</li><li>Jobs</li><li>Help Us Grow</li></ul></div>
<div class="abs foot-col" style="left:547px"><h4>Products</h4><ul><li>Fieldline Projects</li><li>Fieldline Desk</li><li>Fieldline Chat</li></ul></div>
<div class="abs foot-col" style="left:705px"><h4>Resources</h4><ul><li>Desktop Timer App</li><li>Office Apps for Business</li><li>Tablet App</li><li>Phone App</li><li>Mobile App</li></ul></div>
<div class="abs foot-col contact" style="left:901px"><h4>Contact Us</h4><ul>
  <li><svg width="11" height="15" viewBox="0 0 12 16"><path d="M6 0a6 6 0 00-6 6c0 4.5 6 10 6 10s6-5.5 6-10a6 6 0 00-6-6z" fill="#1d4270"/><circle cx="6" cy="6" r="2.2" fill="#fff"/></svg><span style="width:190px">410 Harlow Ave. Suite 7 - Brenton TX. 75019, Dallas</span></li>
  <li><svg width="13" height="13" viewBox="0 0 24 24"><path fill="#1d4270" d="M6.6 10.8a15 15 0 006.6 6.6l2.2-2.2a1 1 0 011-.25 11.4 11.4 0 003.6.57 1 1 0 011 1V20a1 1 0 01-1 1A17 17 0 013 4a1 1 0 011-1h3.5a1 1 0 011 1c0 1.25.2 2.45.57 3.57a1 1 0 01-.25 1z"/></svg><span>555 014 2280</span></li>
  <li><svg width="14" height="14" viewBox="0 0 16 16"><rect x="1" y="4" width="14" height="11" rx="1" fill="#1d4270"/><rect x="4" y="1" width="8" height="4" fill="#1d4270"/><rect x="4" y="8" width="8" height="4" fill="#fff"/></svg><span>555 014 2291</span></li>
  <li><svg width="14" height="11" viewBox="0 0 24 18"><rect width="24" height="18" rx="2" fill="#1d4270"/><path d="M1 2l11 8 11-8" stroke="#fff" stroke-width="2" fill="none"/></svg><a>info@tandor8vale.com/</a></li>
</ul></div>
<div class="abs foot-rule"></div>
<div class="abs copyright">Copyrights © 2016, Tandor8Vale. All rights reserved.</div>
<div class="abs social"><span></span><span></span><span></span><span></span></div>

</body>
</html>
```